Sunward Meadow Co Business Cards

We need Business cards development for our expanding business. Our Company SunwardMeadowCo promotes grain free living through products, services and healthy living concepts. Our Products are:
Non-Grain
Non- GMO
Non- Soy
Gluten-Free
Updates

Project Deadline Extended
Reason: We will need to extend the deadline on our Business Card contest. Thanks, SMC

Industry/Entity Type

Business

```html
<!DOCTYPE html>
<html lang="en">
<head>
<meta charset="utf-8">
<title>Sunward Meadow Co Business Card</title>
<link rel="stylesheet" href="https://fonts.googleapis.com/css2?family=Exo+2:wght@500&family=Oxygen:wght@400;700&display=swap">
<style>
  :root {
    --backdrop: #3a3a3c;
    --card-top: #ffffff;
    --card-bottom: #e9e9e9;
    --green-dark: #1d7a1a;
    --green-mid: #3fae1f;
    --green-light: #8ed93a;
    --text-green: #1f6e17;
    --rule: #3c3c3c;
    --white: #ffffff;
  }
  * { margin: 0; padding: 0; box-sizing: border-box; }
  html, body { width: 1200px; height: 816px; overflow: hidden; }
  body {
    background: var(--backdrop);
    font-family: "Oxygen", sans-serif;
    position: relative;
  }
  .business-card {
    position: absolute;
    left: 100px;
    top: 122px;
    width: 1000px;
    height: 572px;
    border-radius: 48px;
    background: linear-gradient(160deg, var(--card-top) 0%, var(--card-bottom) 100%);
    overflow: hidden;
  }
  .brand {
    position: absolute;
    left: 470px;
    top: 200px;
    width: 440px;
    text-align: center;
  }
  .brand-name {
    font-family: "Oxygen", sans-serif;
    font-weight: 700;
    font-size: 46px;
    letter-spacing: -1px;
    line-height: 1;
    color: var(--green-dark);
  }
  .brand-tagline {
    margin-top: 8px;
    font-size: 15px;
    letter-spacing: 0.5px;
    color: var(--green-dark);
  }
  .divider-rule {
    position: absolute;
    left: 470px;
    right: 0;
    top: 318px;
    height: 4px;
    background: var(--rule);
  }
  .name-band {
    position: absolute;
    left: 0;
    top: 290px;
    width: 470px;
    height: 92px;
    border-radius: 0 46px 46px 0;
    background: linear-gradient(90deg, var(--green-light) 0%, var(--green-mid) 100%);
    color: var(--white);
    font-family: "Exo 2", sans-serif;
    font-weight: 500;
    text-align: right;
    padding: 14px 44px 0 0;
  }
  .person-name { font-size: 30px; letter-spacing: 1px; line-height: 1.1; }
  .person-role { font-size: 20px; letter-spacing: 2px; text-transform: uppercase; margin-top: 4px; }
  .contact-list {
    position: absolute;
    left: 56px;
    top: 430px;
    list-style: none;
  }
  .contact-list li,
  .address {
    display: flex;
    align-items: center;
    gap: 18px;
    font-size: 22px;
    color: var(--text-green);
    line-height: 1.3;
  }
  .contact-list li { margin-bottom: 10px; }
  .icon { width: 22px; height: 22px; flex: none; fill: var(--text-green); }
  .address {
    position: absolute;
    left: 620px;
    top: 398px;
    align-items: flex-start;
  }
  .address .icon { margin-top: 4px; }
</style>
</head>
<body>
  <section class="business-card">
    <div class="brand">
      <div class="brand-name">SunwardMeadowCo</div>
      <div class="brand-tagline">Simple Foods For Every Table</div>
    </div>

    <div class="divider-rule"></div>

    <div class="name-band">
      <div class="person-name">Daniel Harlow</div>
      <div class="person-role">General Manager</div>
    </div>

    <div class="address">
      <svg class="icon" viewBox="0 0 24 24" aria-hidden="true"><path d="M12 3 2 12h3v9h5v-6h4v6h5v-9h3z"/></svg>
      <span>418 Linden Brook Rd,<br>Fairhaven, USA</span>
    </div>

    <ul class="contact-list">
      <li>
        <svg class="icon" viewBox="0 0 24 24" aria-hidden="true"><path d="M6.6 10.8a15.1 15.1 0 0 0 6.6 6.6l2.2-2.2c.3-.3.7-.4 1-.2 1.1.4 2.3.6 3.6.6.6 0 1 .4 1 1V20c0 .6-.4 1-1 1A17 17 0 0 1 3 4c0-.6.4-1 1-1h3.5c.6 0 1 .4 1 1 0 1.3.2 2.5.6 3.600.1.3 0 .7-.2 1z"/></svg>
        <span>+1 (0555) 41-208-76</span>
      </li>
      <li>
        <svg class="icon" viewBox="0 0 24 24" aria-hidden="true"><path d="M2 5h20v14H2zm2 2v.5l8 5 8-5V7zm0 2.8V17h16V9.8l-8 5z"/></svg>
        <span>hello@sunwardmeadow.com</span>
      </li>
      <li>
        <svg class="icon" viewBox="0 0 24 24" aria-hidden="true"><path d="M12 2a10 10 0 1 0 0 20 10 10 0 0 0 0-20zm6.9 9h-3a15 15 0 0 0-1.2-5.6A8 8 0 0 1 18.9 11zM12 4.1c.9 1.2 1.8 3.6 1.9 6.9h-3.8c.1-3.3 1-5.7 1.9-6.9zM9.3 5.4A15 15 0 0 0 8.1 11h-3a8 8 0 0 1 4.2-5.6zM5.1 13h3a15 15 0 0 0 1.2 5.6A8 8 0 0 1 5.1 13zm6.9 6.9c-.9-1.2-1.8-3.6-1.9-6.9h3.8c-.1 3.3-1 5.7-1.9 6.9zm2.7-1.3a15 15 0 0 0 1.2-5.6h3a8 8 0 0 1-4.2 5.6z"/></svg>
        <span>www.sunwardmeadow.com</span>
      </li>
    </ul>
  </section>
</body>
</html>
```